Business Card Design

After a corporate career in the finance sector I am now operating on my own as a consultant. I require a simple design, and want a strong card which is targeted at a conservative audience.

Target Market(s)

highly educated senior management, directors of companies, finance sector

Industry/Entity Type

Conservative

Contact Information for Business Card

Rosa Tindell
Consultant
Mobile: 0417 862 254
Email: rosa.tind@mailvora.com

Requirements
Should not have
• I don't want the colours green/yellow/brown

```html
<!DOCTYPE html>
<html lang="en">
<head>
<meta charset="utf-8">
<title>Rosa Tindell – Business Card</title>
<link href="https://fonts.googleapis.com/css2?family=Gelasio:wght@400;700&display=swap" rel="stylesheet">
<style>
  :root {
    --backdrop: #e4e4e6;
    --card: #ffffff;
    --ink: #1a1a1a;
    --mark: #3a3a3a;
    --rule: #555555;
    --shadow: rgba(0, 0, 0, 0.18);
  }
  * { margin: 0; padding: 0; box-sizing: border-box; }
  html, body {
    width: 1200px;
    height: 873px;
    overflow: hidden;
    background: var(--backdrop);
  }
  .stage {
    width: 1200px;
    height: 873px;
    display: flex;
    align-items: center;
    justify-content: center;
  }
  .business-card {
    width: 840px;
    height: 480px;
    background: var(--card);
    box-shadow: 0 10px 30px var(--shadow);
    position: relative;
    font-family: "Gelasio", Georgia, serif;
    color: var(--ink);
  }
  .identity {
    position: absolute;
    left: 0;
    right: 0;
    top: 62px;
    display: flex;
    flex-direction: column;
    align-items: center;
    text-align: center;
  }
  .brand {
    display: flex;
    align-items: center;
    gap: 12px;
    margin-bottom: 26px;
  }
  .brand-square {
    width: 26px;
    height: 26px;
    background: var(--mark);
  }
  .brand-name {
    font-weight: 700;
    font-size: 30px;
    line-height: 1;
    color: var(--mark);
    letter-spacing: 1px;
  }
  .person-name {
    font-weight: 700;
    font-size: 42px;
    letter-spacing: 0.5px;
    line-height: 1.15;
  }
  .person-role {
    font-weight: 700;
    font-size: 30px;
    line-height: 1.25;
  }
  .divider {
    position: absolute;
    left: 90px;
    right: 90px;
    top: 300px;
    height: 1px;
    background: var(--rule);
  }
  .contact {
    position: absolute;
    left: 0;
    right: 0;
    top: 322px;
    text-align: center;
    font-weight: 700;
    font-size: 24px;
    line-height: 1.55;
  }
  .contact .phone {
    font-size: 21px;
  }
</style>
</head>
<body>
  <main class="stage">
    <article class="business-card">
      <div class="identity">
        <div class="brand">
          <span class="brand-square"></span>
          <span class="brand-name">TINDELL ADVISORY</span>
        </div>
        <h1 class="person-name">ROSA TINDELL</h1>
        <p class="person-role">Consultant</p>
      </div>
      <div class="divider"></div>
      <div class="contact">
        <p class="email">Email | rosa.tind@mailvora.com</p>
        <p class="phone">Mobile | 0417 862 254</p>
      </div>
    </article>
  </main>
</body>
</html>
```